Simple templates for management consulting firm

Vireo Associates is a management consulting firm based in the DC area. We have all the basic templates but would like to tweak them so they look consistent.

Check us out at www.vireoassociates-example.com

For this project we would like to get
a tweaked powerpoint template (header should be up)
a letter template for letters
a fax template

Current templates and our logo are attached.
Updates

We just increased the budget of this project.

We got questions about the project. Here are our thoughts on this one:

Please include the logo into the fax template. If you find improvements in the layout then feel free to make those. Let's not overthink this too much. Keep it simple :)

We like The powerpoint concept as is. The slide titles are for some reasons on the bottom. It seems to irritate some folks. If you can switch the slide titles to the top, keep the look and feel of the slides and work in the logo then that would be fantastic.

The letter head should include the following

Vireo Associates, LLC Box 5827, Millbrook, VA 20147 Phone 703 518-9461, Fax 703 286 7135, www.vireoassociates-example.com and the logo.

Again, let's keep it simple.

Thank you for considering this project.

We just realize that we are not necessarily inisting to use the red in the slides.
Any approach that would work with the logo will be considered.

Thanks for your creativity.

Target Market(s)

tech companies, Pinnacle 400, venture capitalists

Industry/Entity Type

Management Consulting

Requirements
Must have
• Keep it simple please

```html
<!DOCTYPE html>
<html lang="en">
<head>
<meta charset="utf-8">
<title>Vireo Associates – Slide Template</title>
<link href="https://fonts.googleapis.com/css2?family=Fira+Sans+Condensed:wght@300;400;600;700;800&display=swap" rel="stylesheet">
<style>
  :root {
    --slide-light: #f7f7f7;
    --slide-mid: #dcdcdc;
    --slide-edge: #c4c4c4;
    --gap: #ffffff;
    --ink-dark: #3a3a3a;
    --ink-body: #4a4a4a;
    --ink-sub: #565656;
    --ink-title: #a3a3a3;
    --brand-grey: #8c8c8c;
    --gold: #e8bf3c;
    --gold-light: #f2d77a;
    --rule: #9a9a9a;
  }
  * { margin: 0; padding: 0; box-sizing: border-box; }
  html, body { width: 871px; height: 1200px; overflow: hidden; background: var(--gap); }
  body { position: relative; font-family: "Fira Sans Condensed", "Arial Narrow", sans-serif; }

  .slide {
    position: absolute; left: 0; width: 871px;
    background: radial-gradient(ellipse 70% 65% at 50% 45%, var(--slide-light) 0%, var(--slide-mid) 70%, var(--slide-edge) 100%);
    overflow: hidden;
  }
  .slide--title { top: 0; height: 593px; }
  .slide--agenda { top: 607px; height: 593px; }

  .brand { position: absolute; display: flex; align-items: center; }
  .brand__dot { border-radius: 50%; background: var(--brand-grey); flex: none; }
  .brand__name { color: var(--brand-grey); font-weight: 400; line-height: 1; white-space: nowrap; letter-spacing: 0.02em; }
  .brand--large { left: 208px; top: 217px; }
  .brand--large .brand__dot { width: 128px; height: 128px; margin-right: 22px; }
  .brand--large .brand__name { font-size: 50px; }
  .brand--small { left: 311px; top: 1071px - 607px; }
  .slide--agenda .brand--small { left: 311px; top: 464px; }
  .brand--small .brand__dot { width: 76px; height: 76px; margin-right: 14px; }
  .brand--small .brand__name { font-size: 30px; }

  .presenter { position: absolute; left: 0; width: 871px; text-align: center; top: 434px; }
  .presenter__name { font-size: 48px; font-weight: 700; color: var(--ink-dark); line-height: 1; letter-spacing: -0.5px; }
  .presenter__role { font-size: 24px; font-weight: 400; color: var(--ink-dark); line-height: 1; margin-top: 4px; }

  .legal { position: absolute; left: 0; width: 871px; }
  .legal__rule { margin: 0 auto; width: 770px; height: 1px; background: var(--rule); }
  .legal__text { text-align: center; font-size: 12.5px; line-height: 11px; color: var(--ink-dark); margin-top: 4px; letter-spacing: -0.1px; }
  .slide--title .legal { top: 545px; }
  .slide--agenda .legal { top: 545px; }

  .agenda__title {
    position: absolute; left: 0; width: 871px; top: 10px; text-align: center;
    font-size: 64px; font-weight: 800; color: var(--ink-title); line-height: 1;
    text-shadow: 1px 1px 0 #7a7a7a, 2px 3px 3px rgba(0,0,0,0.35);
  }
  .agenda__bar {
    position: absolute; left: 71px; top: 97px; width: 731px; height: 13px;
    background: linear-gradient(90deg, var(--gold) 0%, var(--gold-light) 50%, var(--gold) 100%);
    box-shadow: 0 3px 4px rgba(0,0,0,0.3);
  }
  .agenda__list { position: absolute; left: 0; top: 0; list-style: none; }
  .agenda__item {
    position: absolute; left: 74px; white-space: nowrap;
    font-size: 35px; font-weight: 300; color: var(--ink-body); line-height: 1;
    padding-left: 17px;
  }
  .agenda__item::before {
    content: ""; position: absolute; left: 0; top: 50%; width: 11px; height: 6px; margin-top: -4px;
    border-radius: 2px; background: #7d7d7d;
  }
  .agenda__sub {
    position: absolute; left: 132px; white-space: nowrap;
    font-size: 29px; font-weight: 600; color: var(--ink-sub); line-height: 1;
  }
</style>
</head>
<body>

  <section class="slide slide--title">
    <div class="brand brand--large">
      <span class="brand__dot"></span>
      <span class="brand__name">Vireo Associates</span>
    </div>
    <div class="presenter">
      <p class="presenter__name">Paul Hartwell</p>
      <p class="presenter__role">Managing Partner</p>
    </div>
    <div class="legal">
      <div class="legal__rule"></div>
      <p class="legal__text">Copyright © 2012 by Vireo Associates, LLC. All rights reserved. This document contains confidential and proprietary information and may not be<br>reproduced, in whole or in part, without express written permission from Vireo Associates, LLC.</p>
    </div>
  </section>

  <section class="slide slide--agenda">
    <h1 class="agenda__title">Agenda</h1>
    <div class="agenda__bar"></div>
    <ul class="agenda__list">
      <li class="agenda__item" style="top:152px;">Jumpstart Your Business</li>
      <li class="agenda__sub" style="top:194px;">Mastering the Sale</li>
      <li class="agenda__sub" style="top:231px;">Getting Projects Done</li>
      <li class="agenda__sub" style="top:266px;">Turnaround</li>
      <li class="agenda__item" style="top:307px;">Vireo Associates’ Engagement Model</li>
      <li class="agenda__item" style="top:355px;">About Daniel Reiter</li>
    </ul>
    <div class="brand brand--small">
      <span class="brand__dot"></span>
      <span class="brand__name">Vireo Associates</span>
    </div>
    <div class="legal">
      <div class="legal__rule"></div>
      <p class="legal__text">Copyright © 2012 by Vireo Associates, LLC. All rights reserved. This document contains confidential and proprietary information and may not be<br>reproduced, in whole or in part, without express written permission from Vireo Associates, LLC.</p>
    </div>
  </section>

</body>
</html>
```